Dashboard Elements

Hello – looking for someone to create dashboard elements.
I’ve already basically designed all these elements – but I need someone to take what I’ve designed and make it look like an actual dashboard UI, like an app - assuming using some kind of dashboard UI kit (but however you would like to get it done is fine). It can look just like mine or try something different, as long as it matches the color scheme webpage that I’m going to out it on – see the page here. I’m ok with making it dark, maybe that would look better – again as long as it matches the webpage (https://www.plankora.com/file/7QxVbN2kLmRtWp4Ya8Hc3J/Webpage-with-placeholders?node-id=0%3A1). Please note, you do not need to put anything on the webpage or do anything with this Figma file, this is just a reference so you can color/stylize it accordingly.

The attached Powerpoint file has everything you need - make sure to zoom all the way out to see everything on the slides.

Here are the Dashboard elements needed (this will all make sense when you look at the PPT):
Dashboard 1
Dashboard 1 – expanded view A
Dashboard 1 – expanded view B
View Source button by itself
Source Document Viewer 1 and 2 (these are exactly the same just with a different image inside)*
Dashboard 2 (only slightly different than Dashboard 1, just extended with extra headings
Table of Contents
Searchbar and Source Doc by itself
*the documents in the source document viewers should still look like documents - they don’t need to look like part of the UI, because this is a document viewer – you can restyle/recolor if necessary or just leave these as is.
- Colors must match color scheme of webpage, attached and on Figma link (images there currently are only placeholders) – ok to go dark as long as it matches
- Must look sleek, clean, realistic
- Don’t add any pictures of people or change the text.
- In case it’s not clear, this is what I mean by the concept of Dashboard UI - https://www.quillbary.com/shard/s2/sh/9a4c1e27-b835-4f02-a7d6-5c0e81b3f947/e72b6a09c4d1f5830b9e6a2d7c4f1e58
- Must be sent in an editable file, I may need to be edit text and other elements
- If you are going to send a sample, please make sure it’s part of the dashboard itself, not just the table of contents etc

Ideally hoping to find someone I can continue working with as I'll have a lot more graphic design work needed coming up.

Thank you!

```html
<!DOCTYPE html>
<html lang="en">
<head>
<meta charset="utf-8">
<title>Quendara C-CDA Compendium</title>
<link rel="stylesheet" href="https://fonts.googleapis.com/css2?family=Exo+2:wght@200;300;400;500&family=Ubuntu:wght@300;400;500&family=Roboto:wght@300;400&display=swap">
<style>
:root{
  --bg:#141127;
  --bg-deep:#0f0c20;
  --panel:#221d40;
  --card:#1c1836;
  --band:#17132d;
  --purple:#7d6be3;
  --purple-soft:#9a8cf0;
  --purple-line:#6f5fd6;
  --teal:#2dc8b4;
  --teal-deep:#15a898;
  --text:#ece9fb;
  --muted:#b9b3dc;
}
*{box-sizing:border-box;margin:0;padding:0}
html,body{width:1200px;height:4234px;overflow:hidden;background:var(--bg)}
.canvas{position:relative;width:1200px;height:4234px;overflow:hidden;font-family:"Ubuntu",sans-serif;color:var(--text);
  background:
   radial-gradient(600px 500px at 1150px 1200px,rgba(90,70,180,.35),transparent 70%),
   radial-gradient(700px 600px at 0px 1100px,rgba(40,150,160,.18),transparent 70%),
   radial-gradient(800px 700px at 1200px 3000px,rgba(60,160,150,.25),transparent 70%),
   radial-gradient(900px 700px at 100px 4100px,rgba(40,170,150,.35),transparent 70%),
   radial-gradient(700px 600px at 1100px 4000px,rgba(120,90,220,.3),transparent 70%),
   var(--bg)}
.abs{position:absolute}
.headline{position:absolute;left:0;width:1200px;text-align:center;font-family:"Exo 2",sans-serif;font-weight:300;font-size:40px;letter-spacing:4px;line-height:50px;color:var(--text)}
.label{position:absolute;font-family:"Exo 2",sans-serif;font-size:16px;letter-spacing:2px;font-weight:400}
.copy{position:absolute;font-family:"Roboto",sans-serif;font-weight:300;font-size:15.5px;line-height:26px;color:var(--muted)}
.ball{position:absolute;border-radius:50%;background:radial-gradient(circle at 40% 35%,#3fd6d0,#1aa6b8 55%,#2a5ca0)}
.engine-ring{position:absolute;left:99px;top:236px;width:400px;height:400px;border-radius:50%;background:rgba(40,34,74,.55);border:1px solid rgba(150,140,220,.25)}
.engine-core{position:absolute;left:249px;top:386px;width:100px;height:100px;border-radius:50%;background:radial-gradient(circle,#35c7c2,#4d4bb3 70%,transparent 72%)}

.toc-stage{position:absolute;left:602px;top:580px;width:417px;height:599px;background:var(--panel);overflow:hidden}
.toc-box{position:absolute;left:42px;top:38px;width:334px;height:528px;border:3px solid var(--purple-line);border-radius:18px;background:rgba(28,24,54,.92)}
.toc-head{position:absolute;left:12px;top:9px;width:306px;height:40px;border:2px solid var(--purple-line);border-radius:20px;display:flex;align-items:center;justify-content:center;gap:12px;font-size:21px;color:var(--muted);background:#2a2450}
.toc-list{position:absolute;left:0;top:97px;width:328px;list-style:none}
.toc-list li{height:40px;line-height:36px;padding-left:22px;font-size:17px;color:var(--text)}
.toc-list li.is-active{background:var(--teal);height:36px}

.stage{position:absolute;overflow:hidden;background:var(--panel)}
.blob{position:absolute;border-radius:50%}
.blob.teal{background:var(--teal)}
.blob.purple{background:var(--purple)}
.deco{position:absolute;background:var(--purple);border-radius:6px}
.deco.faint{background:#3a3360}
.card{position:absolute;border:3px solid var(--purple-line);border-radius:36px;background:rgba(28,24,54,.96);overflow:hidden}
.brand{position:absolute;display:flex;align-items:center;gap:7px;font-family:"Ubuntu",sans-serif;font-weight:400;color:var(--text);letter-spacing:1px;white-space:nowrap}
.brand i{display:block;background:var(--purple);border-radius:50%}
.dash-title{position:absolute;font-family:"Ubuntu",sans-serif;color:var(--purple-soft);font-weight:400;white-space:nowrap}
.patient{position:absolute;line-height:1.35;white-space:nowrap}
.patient b{font-weight:400;color:var(--text)}
.patient small{display:block;color:var(--muted)}
.meta{position:absolute;display:flex;align-items:center;white-space:nowrap}
.teal-t{color:var(--teal)}
.count{display:inline-flex;align-items:center;justify-content:center;border:1.5px solid var(--purple);border-radius:50%;color:var(--text)}
.search{position:absolute;border:1.5px solid var(--purple);border-radius:12px;display:flex;align-items:center;gap:6px;padding-left:10px;color:var(--muted)}
.grid{position:absolute;display:grid;align-items:center}
.th{color:var(--text);display:flex;flex-direction:column;gap:5px}
.th span{display:flex;align-items:center;gap:4px;white-space:nowrap}
.th span::after{content:"";display:inline-block;width:.8em;height:.8em;border-radius:50%;background:var(--purple)}
.th em{display:block;height:4px;border-radius:2px;background:var(--purple);width:80%}
.code{color:var(--teal)}
.cond{color:var(--muted)}
.pill{display:inline-flex;align-items:center;justify-content:center;background:var(--purple);border:2px solid #b6abf8;border-radius:10px;color:#fff}
.raf{color:var(--teal);display:flex;align-items:center;gap:12px}
.chev{width:12px;height:8px}
.btn{position:absolute;display:flex;align-items:center;justify-content:center;gap:10px;background:var(--purple-soft);border-radius:20px;color:#fff;font-family:"Ubuntu",sans-serif;white-space:nowrap}
.btn.teal{background:var(--teal)}
.band{position:absolute;left:0;width:100%;background:var(--band)}
.pop{position:absolute;border:3px solid var(--purple-line);border-radius:16px;background:#1b1733;box-shadow:0 0 18px rgba(120,100,230,.5)}
</style>
</head>
<body>
<div class="canvas">

  <h1 class="headline" style="top:72px">TRANSFORMED INTO 1 COMPOSITE<br>C-CDA HEALTH RECORD</h1>
  <svg class="abs" style="left:0;top:0" width="1200" height="1300" fill="none" stroke="rgba(180,170,230,.45)" stroke-width="1.3">
    <path d="M420 290 C470 240 520 200 590 180"/>
    <path d="M440 570 C500 640 470 720 510 780 C550 850 600 860 640 880"/>
  </svg>
  <div class="engine-ring"></div>
  <div class="engine-core" role="img" aria-label="Synthesis engine emblem"></div>
  <div class="ball" style="left:378px;top:280px;width:54px;height:54px"></div>
  <div class="ball" style="left:82px;top:560px;width:76px;height:76px"></div>

  <div class="label" style="left:615px;top:402px">QUENDARA SYNTHESIS ENGINE</div>
  <p class="copy" style="left:615px;top:440px;width:510px">The Quendara synthesis engine utilizes OCR, advanced parsing techniques. Clinical Natural Language Processing (cNLP), proprietary logic and NPI matching to clean, de-duplicate, structure and enrich all inputs from data acquisition.</p>

  <div class="toc-stage">
    <div class="blob purple" style="left:300px;top:200px;width:230px;height:230px;opacity:.7"></div>
    <div class="blob teal" style="left:-60px;top:300px;width:120px;height:220px"></div>
    <div class="blob teal" style="left:360px;top:300px;width:120px;height:120px"></div>
    <div class="toc-box">
      <div class="toc-head">Table of Contents
        <svg width="16" height="10" viewBox="0 0 16 10"><path d="M2 2l6 6 6-6" stroke="#2dc8b4" stroke-width="3" fill="none"/></svg>
      </div>
      <ul class="toc-list">
        <li class="is-active">Insurance Providers</li>
        <li>Problems</li><li>Results</li><li>Procedures</li><li>Encounters</li>
        <li>Medications</li><li>Vital Signs</li><li>Immunizations</li><li>Social History</li><li>Family History</li>
      </ul>
      <div class="deco" style="left:212px;top:420px;width:80px;height:80px"></div>
    </div>
  </div>

  <div class="label" style="left:87px;top:826px">COMPENDIUM C-CDA</div>
  <p class="copy" style="left:87px;top:862px;width:400px">The normalized data is unified into the Compendium C-CDA. Enhanced composite longitudinal record in C-CDA format, the industry standard for all interoperability initiatives.</p>

  <div class="abs" style="left:84px;top:1212px;width:1032px;height:580px;border-radius:12px;background:rgba(40,34,72,.55);border:1px solid rgba(140,130,210,.2)"></div>
  <h2 class="headline" style="top:1278px">SUMMARIZED AND LINKED<br>TO KEY INSIGHTS</h2>
  <p class="copy" style="left:250px;top:1398px;width:700px;text-align:center">Insights are presented in a concise summary with direct links to supporting evidence. HCC opportunities are abstracted and cross-linked directly to the original text in the underlying record for quick and easy reference.</p>

  <div class="stage" style="left:229px;top:1508px;width:744px;height:448px">
    <div class="blob teal" style="left:-40px;top:140px;width:110px;height:220px"></div>
    <div class="blob purple" style="left:650px;top:120px;width:200px;height:220px"></div>
    <div class="card" style="left:39px;top:37px;width:671px;height:373px;border-radius:30px">
      <div class="brand" style="left:34px;top:25px;font-size:15px"><i style="width:14px;height:14px"></i>QUENDARA</div>
      <div class="dash-title" style="left:200px;top:16px;font-size:27px">C-CDA Compendium</div>
      <div class="patient" style="left:512px;top:18px;font-size:11px"><b>Patient, Mary</b><small style="font-size:7px">Female | 01/11/1951 | Age: 70</small></div>
      <div class="deco" style="left:30px;top:100px;width:72px;height:72px"></div>
      <div class="deco faint" style="left:30px;top:255px;width:50px;height:50px"></div>
      <div class="meta" style="left:156px;top:76px;font-size:11px;gap:6px"><svg class="chev" viewBox="0 0 12 8"><path d="M2 2l4 4 4-4" stroke="#2dc8b4" stroke-width="2" fill="none"/></svg>HCC Summary</div>
      <div class="search" style="left:272px;top:72px;width:142px;height:22px;font-size:7px"><svg width="9" height="9" viewBox="0 0 10 10"><circle cx="4" cy="4" r="3" stroke="#2dc8b4" fill="none" stroke-width="1.5"/><path d="M6.5 6.5l3 3" stroke="#2dc8b4" stroke-width="1.5"/></svg>Search...</div>
      <div class="meta" style="left:440px;top:77px;font-size:8px;gap:10px"><span class="teal-t">RAF: 2.362</span><span>Condition Count <span class="count" style="width:16px;height:16px;font-size:9px">8</span></span><span class="teal-t">ID: 7326472</span></div>
      <div class="grid" style="left:174px;top:118px;grid-template-columns:138px 156px 107px 90px;grid-auto-rows:36px;font-size:8px">
        <div class="th"><span>ICD-10 Code</span><em></em></div><div class="th"><span>Condition</span><em></em></div><div class="th"><span>Category</span><em style="width:60%"></em></div><div class="th"><span>RAF</span><em style="width:40%"></em></div>
        <div class="code" style="font-size:12px">J44.9</div><div class="cond" style="font-size:6px">Chronic obstructive pulmonary disease</div><div><span class="pill" style="width:70px;height:17px;font-size:7px">111</span></div><div class="raf" style="font-size:12px">0.335<svg class="chev" viewBox="0 0 12 8"><path d="M2 2l4 4 4-4" stroke="#fff" stroke-width="2" fill="none"/></svg></div>
        <div class="code" style="font-size:12px">F33.1</div><div class="cond" style="font-size:6px">Chronic kidney disease, moderate (stage 3)</div><div><span class="pill" style="width:70px;height:17px;font-size:7px">138</span></div><div class="raf" style="font-size:12px">0.069<svg class="chev" viewBox="0 0 12 8"><path d="M2 2l4 4 4-4" stroke="#fff" stroke-width="2" fill="none"/></svg></div>
        <div class="code" style="font-size:12px">F33.0</div><div class="cond" style="font-size:6px">Major depressive disorder, recurrent, mild</div><div><span class="pill" style="width:70px;height:17px;font-size:7px">59</span></div><div class="raf" style="font-size:12px">0.309<svg class="chev" viewBox="0 0 12 8"><path d="M2 2l4 4 4-4" stroke="#fff" stroke-width="2" fill="none"/></svg></div>
        <div class="code" style="font-size:12px">I42.9</div><div class="cond" style="font-size:6px">cardiomyopathy</div><div><span class="pill" style="width:70px;height:17px;font-size:7px">85</span></div><div class="raf" style="font-size:12px">0.447<svg class="chev" viewBox="0 0 12 8"><path d="M2 2l4 4 4-4" stroke="#fff" stroke-width="2" fill="none"/></svg></div>
        <div class="code" style="font-size:12px">E11.36</div><div class="cond" style="font-size:6px">Type 2 diabetes mellitus with diabetic cataract</div><div><span class="pill" style="width:70px;height:17px;font-size:7px">18</span></div><div class="raf" style="font-size:12px">0.302<svg class="chev" viewBox="0 0 12 8"><path d="M2 2l4 4 4-4" stroke="#fff" stroke-width="2" fill="none"/></svg></div>
      </div>
    </div>
  </div>

  <div class="stage" style="left:71px;top:1986px;width:1062px;height:641px">
    <div class="blob teal" style="left:-120px;top:220px;width:300px;height:330px"></div>
    <div class="blob purple" style="left:920px;top:160px;width:300px;height:300px"></div>
    <div class="blob teal" style="left:740px;top:470px;width:400px;height:300px"></div>
    <div class="deco" style="left:38px;top:40px;width:86px;height:86px"></div>
    <div class="card" style="left:158px;top:53px;width:766px;height:537px">
      <div class="meta" style="left:60px;top:48px;font-size:17px"><span class="code">E11.36</span></div>
      <div class="meta" style="left:200px;top:52px;font-size:11px">Type 2 diabetes mellitus with diabetic cataract</div>
      <span class="pill abs" style="left:466px;top:46px;width:96px;height:24px;font-size:11px">18</span>
      <div class="meta teal-t" style="left:626px;top:48px;font-size:17px;gap:20px">0.302<svg class="chev" viewBox="0 0 12 8" style="width:14px"><path d="M2 6l4-4 4 4" stroke="#fff" stroke-width="2.2" fill="none"/></svg></div>
      <div class="abs" style="left:0;top:92px;width:100%;text-align:center;font-size:11px;color:var(--muted)"><b style="color:var(--text);font-weight:500">Why:</b> This Patient was treated for cataracts that may be associated with type 2 diabetes mellitus</div>
      <div class="band" style="top:138px;height:72px"></div>
      <div class="meta" style="left:65px;top:165px;font-size:13px">Extacpsular cataract With IOL</div>
      <div class="meta" style="left:320px;top:165px;font-size:13px">C-CDA: Procedures</div>
      <div class="band" style="top:320px;height:76px"></div>
      <div class="meta" style="left:65px;top:350px;font-size:13px">Diabetes Type 2</div>
      <div class="meta" style="left:320px;top:350px;font-size:13px">C-CDA: Problem list</div>
    </div>
    <div class="btn" style="left:682px;top:211px;width:174px;height:36px;font-size:16px"><svg width="18" height="16" viewBox="0 0 18 16"><path d="M1 15h16M4 13V8M8 13V5M12 13V9M15 13V3" stroke="#fff" stroke-width="2"/></svg>View Source</div>
    <div class="btn" style="left:682px;top:392px;width:174px;height:36px;font-size:16px"><svg width="18" height="16" viewBox="0 0 18 16"><path d="M1 15h16M4 13V8M8 13V5M12 13V9M15 13V3" stroke="#fff" stroke-width="2"/></svg>View Source</div>
    <div class="pop" style="left:33px;top:265px;width:619px;height:108px">
      <div class="meta" style="left:50px;top:44px;font-size:12px;color:var(--purple-soft)">Cataract</div>
      <div class="abs" style="left:185px;top:24px;font-size:11px;line-height:14px"><span style="color:var(--purple-soft);font-size:12px">Ophthalmology Chart Note</span><br>Patient presents for cataract<br>evaluation in the right eye.</div>
      <div class="btn teal" style="left:422px;top:36px;width:146px;height:32px;font-size:13px"><svg width="15" height="13" viewBox="0 0 18 16"><path d="M1 15h16M4 13V8M8 13V5M12 13V9M15 13V3" stroke="#fff" stroke-width="2"/></svg>View Source</div>
    </div>
    <div class="pop" style="left:406px;top:452px;width:616px;height:105px">
      <div class="meta" style="left:48px;top:40px;font-size:12px;color:var(--teal)">HbA1c</div>
      <div class="abs" style="left:183px;top:17px;font-size:11px;line-height:14px"><span style="color:var(--purple-soft);font-size:12px">Lab Results</span><br>Hemoglobin A1C<br>6.9%<br>01/15/21</div>
      <div class="btn teal" style="left:419px;top:34px;width:146px;height:32px;font-size:13px"><svg width="15" height="13" viewBox="0 0 18 16"><path d="M1 15h16M4 13V8M8 13V5M12 13V9M15 13V3" stroke="#fff" stroke-width="2"/></svg>View Source</div>
    </div>
    <div class="deco" style="left:972px;top:570px;width:52px;height:46px;background:var(--teal)"></div>
  </div>

  <div class="stage" style="left:71px;top:2680px;width:1055px;height:498px">
    <div class="blob teal" style="left:-60px;top:260px;width:330px;height:330px"></div>
    <div class="blob teal" style="left:880px;top:210px;width:300px;height:300px"></div>
    <div class="deco" style="left:34px;top:22px;width:84px;height:84px"></div>
    <div class="card" style="left:156px;top:52px;width:761px;height:378px">
      <div class="meta code" style="left:61px;top:48px;font-size:17px">N18.31</div>
      <div class="meta" style="left:202px;top:52px;font-size:11px">Chronic kidney disease, stage 3a</div>
      <span class="pill abs" style="left:465px;top:46px;width:97px;height:24px;font-size:11px">138</span>
      <div class="meta teal-t" style="left:626px;top:48px;font-size:17px;gap:20px">0.069<svg class="chev" viewBox="0 0 12 8" style="width:14px"><path d="M2 6l4-4 4 4" stroke="#fff" stroke-width="2.2" fill="none"/></svg></div>
      <div class="abs" style="left:0;top:92px;width:100%;text-align:center;font-size:11px;color:var(--muted)"><b style="color:var(--text);font-weight:500">Why:</b> This patient has an eGFR between 45-59 mL/min</div>
      <div class="band" style="top:140px;height:86px"></div>
      <div class="meta" style="left:67px;top:180px;font-size:12px">eGFR</div>
      <div class="abs" style="left:320px;top:160px;font-size:11px;line-height:17px"><span style="font-size:12px">Lab Results</span><br>47mL/min<br>05/26/2021</div>
      <div class="btn" style="left:523px;top:166px;width:172px;height:36px;font-size:16px"><svg width="18" height="16" viewBox="0 0 18 16"><path d="M1 15h16M4 13V8M8 13V5M12 13V9M15 13V3" stroke="#fff" stroke-width="2"/></svg>View Source</div>
      <div class="abs" style="left:248px;top:232px;width:262px;height:4px;background:var(--teal);border-radius:2px"></div>
      <div class="abs" style="left:0;top:254px;width:100%;text-align:center;font-size:12px;color:var(--purple-soft)">History</div>
      <div class="abs" style="left:320px;top:274px;font-size:11px;line-height:18px">45 mL/min&nbsp;&nbsp;&nbsp;03/17/21<br>41 mL/min&nbsp;&nbsp;&nbsp;01/14/21<br>52 mL/min&nbsp;&nbsp;&nbsp;10/15/20<br>44 mL/min&nbsp;&nbsp;&nbsp;06/22/20</div>
    </div>
    <div class="deco" style="left:915px;top:430px;width:52px;height:46px;background:var(--teal)"></div>
  </div>

  <div class="stage" style="left:136px;top:3230px;width:931px;height:956px">
    <div class="blob teal" style="left:-60px;top:640px;width:300px;height:360px"></div>
    <div class="blob purple" style="left:820px;top:620px;width:240px;height:320px"></div>
    <div class="card" style="left:50px;top:41px;width:838px;height:865px">
      <div class="brand" style="left:41px;top:36px;font-size:20px"><i style="width:18px;height:18px"></i>QUENDARA</div>
      <div class="dash-title" style="left:251px;top:22px;font-size:37px">C-CDA Compendium</div>
      <div class="patient" style="left:641px;top:30px;font-size:15px"><b>Patient, Mary</b><small style="font-size:9px">Female | 01/11/1951 | Age: 70</small></div>
      <div class="deco" style="left:36px;top:160px;width:92px;height:110px"></div>
      <div class="deco faint" style="left:34px;top:400px;width:70px;height:60px"></div>
      <div class="meta" style="left:196px;top:98px;font-size:14px;gap:8px"><svg class="chev" viewBox="0 0 12 8"><path d="M2 2l4 4 4-4" stroke="#2dc8b4" stroke-width="2" fill="none"/></svg>HCC Summary</div>
      <div class="abs" style="left:342px;top:94px;width:179px;height:24px;border:1.5px solid var(--purple);border-radius:12px;font-size:10px;color:var(--purple-soft);display:flex;align-items:center;justify-content:center">Newly Identified ICD-10 Codes</div>
      <div class="meta" style="left:552px;top:100px;font-size:10px;gap:14px"><span class="teal-t">RAF: 2.362</span><span>Condition Count <span class="count" style="width:20px;height:20px;font-size:12px">8</span></span><span class="teal-t">ID: 7326472</span></div>
      <div class="grid" style="left:216px;top:154px;grid-template-columns:174px 193px 136px 100px;grid-auto-rows:44.5px;font-size:11px">
        <div class="th"><span>ICD-10 Code</span><em></em></div><div class="th"><span>Condition</span><em style="width:55%"></em></div><div class="th"><span>Catagory</span><em style="width:65%"></em></div><div class="th"><span>RAF</span><em style="width:55%"></em></div>
        <div class="code" style="font-size:16px">I70.0</div><div class="cond" style="font-size:8px">Aortic Atherosclerosis</div><div><span class="pill" style="width:86px;height:20px;font-size:9px">108</span></div><div class="raf" style="font-size:16px">0.298<svg class="chev" viewBox="0 0 12 8"><path d="M2 2l4 4 4-4" stroke="#fff" stroke-width="2" fill="none"/></svg></div>
        <div class="code" style="font-size:16px">F33.1</div><div class="cond" style="font-size:8px">Major depressive disorder, recurrent, mild</div><div><span class="pill" style="width:86px;height:20px;font-size:9px">58</span></div><div class="raf" style="font-size:16px">0.309<svg class="chev" viewBox="0 0 12 8"><path d="M2 2l4 4 4-4" stroke="#fff" stroke-width="2" fill="none"/></svg></div>
        <div class="code" style="font-size:16px">I48.2</div><div class="cond" style="font-size:8px">Cronic Artial Fibrillation</div><div><span class="pill" style="width:86px;height:20px;font-size:9px">96</span></div><div class="raf" style="font-size:16px">0.268<svg class="chev" viewBox="0 0 12 8"><path d="M2 2l4 4 4-4" stroke="#fff" stroke-width="2" fill="none"/></svg></div>
        <div class="code" style="font-size:16px">I20.9</div><div class="cond" style="font-size:8px">Angina Pectoris</div><div><span class="pill" style="width:86px;height:20px;font-size:9px">88</span></div><div class="raf" style="font-size:16px">.14<svg class="chev" viewBox="0 0 12 8" style="margin-left:26px"><path d="M2 2l4 4 4-4" stroke="#fff" stroke-width="2" fill="none"/></svg></div>
      </div>
      <div class="abs" style="left:334px;top:392px;width:195px;height:24px;border:1.5px solid var(--purple);border-radius:12px;font-size:10px;color:var(--purple-soft);display:flex;align-items:center;justify-content:center">Previously Known ICD-10 Codes</div>
      <div class="grid" style="left:216px;top:443px;grid-template-columns:174px 193px 136px 100px;grid-auto-rows:45px;font-size:11px">
        <div class="th"><span>ICD-10 Code</span><em></em></div><div class="th"><span>Condition</span><em style="width:55%"></em></div><div class="th"><span>Catagory</span><em style="width:65%"></em></div><div class="th"><span>RAF</span><em style="width:55%"></em></div>
        <div class="code" style="font-size:16px">F32.9</div><div class="cond" style="font-size:8px">Major Depressive Disorder, Single Episode, Unspecified</div><div><span class="pill" style="width:86px;height:20px;font-size:9px">n/a</span></div><div class="raf" style="font-size:16px">0<svg class="chev" viewBox="0 0 12 8" style="margin-left:38px"><path d="M2 2l4 4 4-4" stroke="#fff" stroke-width="2" fill="none"/></svg></div>
        <div class="code" style="font-size:16px">Z79.01</div><div class="cond" style="font-size:8px">Long-term use of anticoagulants</div><div><span class="pill" style="width:86px;height:20px;font-size:9px">n/a</span></div><div class="raf" style="font-size:16px">0<svg class="chev" viewBox="0 0 12 8" style="margin-left:38px"><path d="M2 2l4 4 4-4" stroke="#fff" stroke-width="2" fill="none"/></svg></div>
        <div class="code" style="font-size:16px">I25.9</div><div class="cond" style="font-size:8px">Chronic ischemic heart disease, unspecified</div><div><span class="pill" style="width:86px;height:20px;font-size:9px">n/a</span></div><div class="raf" style="font-size:16px">0<svg class="chev" viewBox="0 0 12 8" style="margin-left:38px"><path d="M2 2l4 4 4-4" stroke="#fff" stroke-width="2" fill="none"/></svg></div>
        <div class="code" style="font-size:16px">D45</div><div class="cond" style="font-size:8px">Polycythemia vera</div><div><span class="pill" style="width:86px;height:20px;font-size:9px">48</span></div><div class="raf" style="font-size:16px">0.312<svg class="chev" viewBox="0 0 12 8"><path d="M2 2l4 4 4-4" stroke="#fff" stroke-width="2" fill="none"/></svg></div>
      </div>
      <div class="grid" style="left:36px;top:697px;grid-template-columns:153px 125px 112px 97px 85px 112px 90px;grid-auto-rows:45px;font-size:10px">
        <div class="th"><span>ICD-10 Code</span><em></em></div><div class="th"><span>Condition</span><em style="width:75%"></em></div><div class="th"><span>Catagory</span><em style="width:80%"></em></div><div class="th"><span>Predicted %</span><em></em></div><div class="th"><span>Cohort %</span><em style="width:85%"></em></div><div class="th"><span>Difference %</span><em style="width:70%"></em></div><div class="th"><span>Change</span><em style="width:60%"></em></div>
        <div class="code" style="font-size:15px">F32.9</div><div class="cond" style="font-size:8px">Hypertensive heart disease</div><div><span class="pill" style="width:86px;height:20px;font-size:9px">50.2</span></div>
        <div><svg width="76" height="20"><rect width="76" height="20" rx="10" fill="#fff"/><rect width="50" height="20" rx="10" fill="#7d6be3"/><text x="10" y="13" font-size="7" fill="#fff" font-family="Ubuntu">72.7%</text></svg></div>
        <div><svg width="76" height="20"><rect width="76" height="20" rx="10" fill="#fff"/><rect width="24" height="20" rx="10" fill="#7d6be3"/><text x="4" y="13" font-size="7" fill="#fff" font-family="Ubuntu">22.5%</text></svg></div>
        <div><svg width="76" height="20"><rect width="76" height="20" rx="10" fill="#fff"/><rect width="50" height="20" rx="10" fill="#7d6be3"/><text x="10" y="13" font-size="7" fill="#fff" font-family="Ubuntu">72.7%</text></svg></div>
        <div class="code" style="font-size:15px">3.23</div>
        <div class="code" style="font-size:15px">I20.9</div><div class="cond" style="font-size:8px">Type 2 diabetes mellitus</div><div><span class="pill" style="width:86px;height:20px;font-size:9px">3.4</span></div>
        <div><svg width="76" height="20"><rect width="76" height="20" rx="10" fill="#fff"/><rect width="38" height="20" rx="10" fill="#7d6be3"/><text x="8" y="13" font-size="7" fill="#fff" font-family="Ubuntu">56.8%</text></svg></div>
        <div><svg width="76" height="20"><rect width="76" height="20" rx="10" fill="#fff"/><rect width="30" height="20" rx="10" fill="#7d6be3"/><text x="8" y="13" font-size="7" fill="#fff" font-family="Ubuntu">53.4</text></svg></div>
        <div><svg width="76" height="20"><rect width="76" height="20" rx="10" fill="#fff"/><rect width="38" height="20" rx="10" fill="#7d6be3"/><text x="8" y="13" font-size="7" fill="#fff" font-family="Ubuntu">56.8%</text></svg></div>
        <div class="code" style="font-size:15px">1.06</div>
      </div>
    </div>
  </div>

</div>
</body>
</html>
```